Psychologist Banner Ads for Remarketing & yarnwave

Brand awareness campaign for tallowbridge.com.au

// Ad Formats //
Static JPEG
Max 45KB in file size
All ads must have a border

// Ad Sizes //
Static: (for Zindle Display network) 300×250, 160×600, 728×90
Static: (for Yarnwave, no more than 25% text): 600×315, 1200 x 627

Please use logo, image and "maximise your wellbeing" from the website home page.

```html
<!DOCTYPE html>
<html lang="en">
<head>
<meta charset="utf-8">
<title>Tallowbridge Psychology – Banner Set</title>
<link rel="stylesheet" href="https://fonts.googleapis.com/css2?family=Mulish:ital,wght@1,400&family=Lato:wght@700&display=swap">
<style>
  :root {
    --backdrop: #3c2415;
    --border: #ffffff;
    --sky-top: #cfe8f2;
    --sky-mid: #dcedf5;
    --sky-low: #eef6fa;
    --warm-light: #e8d6cb;
    --warm: #cfae9a;
    --warm-deep: #a98472;
    --cloth: #f7f9fb;
    --ink: #2b2f36;
    --brand: #23418f;
    --arc: #2a5aa0;
  }
  * { margin: 0; padding: 0; box-sizing: border-box; }
  html, body { width: 1200px; height: 1051px; overflow: hidden; }
  body { background: var(--backdrop); position: relative; }

  .ad { position: absolute; background: var(--border); padding: 6px; overflow: hidden; }
  .ad__inner { position: relative; width: 100%; height: 100%; overflow: hidden; background: #fff; }

  .ad__photo { position: absolute; }

  .tagline {
    position: absolute;
    font-family: "Mulish", sans-serif;
    font-style: italic;
    font-weight: 400;
    color: var(--ink);
    letter-spacing: 0.09em;
    text-align: center;
    line-height: 1.3;
  }

  .brand {
    position: absolute;
    font-family: "Lato", sans-serif;
    font-weight: 700;
    color: var(--brand);
    text-align: center;
    line-height: 1.1;
  }
  .brand__sub { display: block; letter-spacing: 0.16em; }

  .arc { position: absolute; left: 0; width: 100%; }

  /* Skyscraper 160x600 */
  .ad--sky { left: 156px; top: 52px; width: 206px; height: 778px; }
  .ad--sky .ad__photo {
    left: 0; top: 0; width: 100%; height: 640px;
    background:
      linear-gradient(90deg, rgba(169,132,114,.55) 0%, rgba(207,174,154,.25) 35%, rgba(207,174,154,0) 60%, rgba(207,174,154,.25) 85%, rgba(207,174,154,.45) 100%) 0 370px / 100% 270px no-repeat,
      linear-gradient(180deg, var(--sky-top) 0%, var(--sky-mid) 45%, var(--sky-low) 57%, var(--warm-light) 66%, var(--warm) 78%, var(--cloth) 92%, var(--cloth) 100%);
  }
  .ad--sky .tagline { left: 0; right: 0; top: 70px; font-size: 27px; }
  .ad--sky .arc { top: 585px; height: 60px; }
  .ad--sky .brand { left: 0; right: 0; top: 642px; font-size: 30px; }
  .ad--sky .brand__sub { font-size: 15px; margin-top: 6px; }

  /* Medium rectangle 300x250 */
  .ad--rect { left: 412px; top: 504px; width: 388px; height: 322px; }
  .ad--rect .ad__photo {
    left: 0; top: 0; width: 100%; height: 270px;
    background:
      linear-gradient(90deg, rgba(207,174,154,.5) 0%, rgba(207,174,154,.15) 20%, rgba(207,174,154,.35) 35%, rgba(169,132,114,.6) 48%, rgba(207,174,154,.35) 62%, rgba(207,174,154,.15) 78%, rgba(207,174,154,.4) 92%, rgba(207,174,154,0) 100%) 0 60px / 100% 210px no-repeat,
      linear-gradient(180deg, var(--sky-top) 0%, var(--sky-mid) 30%, var(--warm-light) 55%, var(--sky-low) 78%, var(--cloth) 100%);
  }
  .ad--rect .tagline { left: 0; right: 0; top: 14px; font-size: 21px; }
  .ad--rect .arc { top: 222px; height: 60px; }
  .ad--rect .brand { left: 0; right: 0; top: 250px; font-size: 22px; }
  .ad--rect .brand__sub { font-size: 11px; margin-top: 3px; }

  /* Leaderboard 728x90 */
  .ad--leader { left: 150px; top: 861px; width: 943px; height: 114px; }
  .ad--leader .ad__photo {
    left: 0; top: 0; width: 712px; height: 100%;
    background:
      linear-gradient(180deg, rgba(255,255,255,0) 0%, rgba(255,255,255,0) 70%, rgba(247,249,251,.8) 100%),
      linear-gradient(90deg, var(--sky-mid) 0%, var(--sky-low) 22%, var(--warm-light) 32%, var(--sky-mid) 45%, var(--warm) 56%, var(--warm-deep) 62%, var(--warm) 70%, var(--sky-mid) 80%, var(--warm-light) 92%, var(--sky-low) 100%);
  }
  .ad--leader .tagline { left: 26px; width: 150px; top: 13px; font-size: 20px; }
  .ad--leader .bracket { position: absolute; left: 700px; top: 0; width: 24px; height: 100%; }
  .ad--leader .brand { left: 738px; width: 192px; top: 22px; font-size: 29px; }
  .ad--leader .brand__sub { font-size: 14px; margin-top: 4px; }
</style>
</head>
<body>

<section class="ad ad--sky" aria-label="Skyscraper banner">
  <div class="ad__inner">
    <div class="ad__photo" role="img" aria-label="Photo of a joyful woman with raised arms against a bright sky"></div>
    <p class="tagline">maximise<br>your<br>wellbeing</p>
    <svg class="arc" viewBox="0 0 194 60" preserveAspectRatio="none" aria-hidden="true">
      <path d="M0 38 Q97 -2 194 38 L194 60 L0 60 Z" fill="#fff"/>
      <path d="M0 38 Q97 -2 194 38" fill="none" stroke="var(--arc)" stroke-width="4"/>
    </svg>
    <p class="brand">Tallowbridge<span class="brand__sub">PSYCHOLOGY</span></p>
  </div>
</section>

<section class="ad ad--rect" aria-label="Medium rectangle banner">
  <div class="ad__inner">
    <div class="ad__photo" role="img" aria-label="Photo of a joyful woman with raised arms against a bright sky"></div>
    <p class="tagline">maximise your wellbeing</p>
    <svg class="arc" viewBox="0 0 376 60" preserveAspectRatio="none" aria-hidden="true">
      <path d="M0 40 Q188 -8 376 40 L376 60 L0 60 Z" fill="#fff"/>
      <path d="M0 40 Q188 -8 376 40" fill="none" stroke="var(--arc)" stroke-width="4"/>
    </svg>
    <p class="brand">Tallowbridge<span class="brand__sub">PSYCHOLOGY</span></p>
  </div>
</section>

<section class="ad ad--leader" aria-label="Leaderboard banner">
  <div class="ad__inner">
    <div class="ad__photo" role="img" aria-label="Photo of a joyful woman with outstretched arms against a bright sky"></div>
    <p class="tagline">maximise<br>your<br>wellbeing</p>
    <svg class="bracket" viewBox="0 0 24 102" preserveAspectRatio="none" aria-hidden="true">
      <path d="M0 0 L18 0 Q6 51 18 102 L0 102 Z" fill="#fff"/>
      <path d="M18 0 Q6 51 18 102" fill="none" stroke="var(--arc)" stroke-width="4"/>
    </svg>
    <p class="brand">Tallowbridge<span class="brand__sub">PSYCHOLOGY</span></p>
  </div>
</section>

</body>
</html>
```